Quorvane Brelkit (Logo and Website)

Design a logo and a website for the Quorvane Brelkit project.

https://projects.quorvane.example/projects/iot.brelkit

Brelkit is a runtime and tooling for web technology that enables easy creation of applications for the Internet of Things (embedded computers in physical objects).

It is the official reference implementation of the Z9K Mesh of Gadgets Study Circle and will become one the Quorvane IoT open source projects (see https://iot.quorvane.example/projects/)

Domain: Web Technology, Internet of Things (IoT), Networked Embedded, Security?

Target Market(s)

Web Technology, Internet of Things (IoT)

Logo Text

brelkit

Coding

Coded - Design and coding required

Number of Pages Required

1 page

Colors

Designer to choose colors to be used in the design.

Requirements
Must have
• Decorations should be machine-centric (industrial, home-automation, machine-2-machine, ...)
Nice to have
• # Possible Colors for Logo
• Petrol (see MoG logo, https://www.z9k.example/MoG/IG/wiki/images/4/40/Mog-large.png)
• Should not conflict with #4A7B7C and #A1C5C4 and #009999;
• may contain #4A7B7C and/or #A1C5C4.
• # Website
• We plan to use hugo (https://tarnspin.example/) for building the website. An appropriate template for it would be nice.

```html
<!DOCTYPE html>
<html lang="en">
<head>
<meta charset="utf-8">
<title>Brelkit – Web Technology for the Internet of Things</title>
<link rel="stylesheet" href="https://fonts.googleapis.com/css2?family=Lato:ital,wght@0,400;0,700;1,400&display=swap">
<style>
:root{
  --teal:#2ea58f;
  --teal-dark:#1f8a77;
  --teal-soft:#47b09b;
  --teal-pale:#d7f1ea;
  --ink:#444;
  --ink-soft:#666;
  --white:#fff;
  --footer-bg:#efefef;
  --bar-bg:#dcdcdc;
  --brand-grey:#9a9a9a;
}
*{box-sizing:border-box;margin:0;padding:0}
html,body{width:1200px;height:3046px;overflow:hidden}
body{position:relative;font-family:'Lato',sans-serif;color:var(--ink);background:var(--white)}
.abs{position:absolute}
.btn{position:absolute;display:flex;align-items:center;justify-content:center;font:700 13px 'Lato',sans-serif;letter-spacing:.5px;text-transform:uppercase;border-radius:3px}
.btn-light{border:2px solid var(--white);color:var(--white)}
.btn-teal{border:2px solid var(--teal);color:var(--teal)}
.arrow-circle{position:absolute;border-radius:50%;display:flex;align-items:center;justify-content:center}

/* hero */
.hero{position:absolute;left:0;top:0;width:1200px;height:660px;clip-path:polygon(0 0,1200px 0,1200px 538px,0 654px);
  background:linear-gradient(120deg,#3db79f 0%,#2fa58e 45%,#27927f 100%)}
.brand{position:absolute;display:flex;align-items:center;gap:12px;font-weight:700}
.brand-dot{border-radius:50%}
.hero .brand{left:128px;top:28px;color:var(--white);font-size:36px}
.hero .brand-dot{width:70px;height:70px;border:3px solid var(--white)}
.nav{position:absolute;top:40px;right:125px;display:flex;gap:28px;font-size:17px;color:var(--white)}
.nav .active{border-top:3px solid var(--white);padding-top:0;margin-top:-40px;padding-top:37px}
.hero-title{left:145px;top:238px;color:var(--white);font-weight:700;line-height:1.15}
.hero-title .big{font-size:44px;display:block}
.hero-title .mid{font-size:32px;display:block}
.hero-text{left:145px;top:336px;width:430px;color:var(--white);font-size:16px;line-height:1.55}
.hero-visual{left:410px;top:128px;width:680px;height:370px;border-radius:6px;background:linear-gradient(160deg,#1b2a36,#0f1a22 60%,#c8ccd0 95%)}
.hero .arrow-circle{width:50px;height:50px;border:2px solid var(--white);top:316px}

/* section headings */
.heading{position:absolute;left:0;width:1200px;text-align:center;font-size:30px}
.divider{position:absolute;left:450px;width:300px;height:30px}

/* what we do */
.wwd-text{left:200px;top:730px;width:800px;text-align:center;font-size:16px;line-height:1.7;color:var(--ink-soft)}
.wwd-visual{left:330px;top:895px;width:540px;height:280px;border-radius:270px 270px 0 0;background:radial-gradient(circle at 50% 70%,#c7ece1,#e6f7f2 70%)}

/* why we are */
.why{position:absolute;left:0;top:1175px;width:1200px;height:445px;background:linear-gradient(110deg,#3aa891,#2d9a84 55%,#3aa891)}
.why-title{left:122px;top:82px;font-size:32px;color:var(--white)}
.why-text{left:122px;top:138px;width:470px;font-size:16px;line-height:1.7;color:var(--white)}
.why-text p+p{margin-top:10px}
.why-visual{left:590px;top:70px;width:485px;height:290px;border-radius:6px;background:linear-gradient(180deg,#222,#111 88%,#ccc 88%)}

/* projects */
.card{position:absolute;top:1752px;width:298px;height:308px;background:var(--white);box-shadow:0 2px 8px rgba(0,0,0,.22)}
.card-img{width:298px;height:186px;background:linear-gradient(135deg,#1d2f4a,#3a6a90)}
.card-title{margin-top:18px;text-align:center;font-size:20px;color:var(--ink-soft)}
.card-text{margin:8px auto 0;width:250px;text-align:center;font-size:12px;line-height:1.7;color:var(--ink-soft)}
.card .arrow-circle{width:38px;height:38px;background:var(--teal);left:130px;bottom:-19px}

/* testimonials */
.testi{position:absolute;left:0;top:2143px;width:1200px;height:457px;background:linear-gradient(120deg,#53b9a3,#3aa690 55%,#4fb59f)}
.quote{position:absolute;top:167px;width:295px;height:220px;border:1.5px solid rgba(255,255,255,.85);color:var(--white);text-align:center}
.quote p{margin:42px auto 0;width:240px;font-style:italic;font-size:13px;line-height:1.85}
.quote .name{margin-top:10px;font-weight:700;font-size:17px}
.avatar{position:absolute;top:-40px;left:107px;width:82px;height:82px;border-radius:50%;border:3px solid var(--white);background:linear-gradient(180deg,#dfe6e4,#a9bcb8)}
.testi .arrow-circle{width:36px;height:36px;top:284px;background:rgba(255,255,255,.35)}

/* partners */
.partners{position:absolute;left:0;top:2600px;width:1200px;height:102px;display:flex;align-items:center;justify-content:space-around;padding:0 120px;color:var(--brand-grey);font-size:26px;font-weight:700}

/* footer */
.footer{position:absolute;left:0;top:2702px;width:1200px;height:276px;background:var(--footer-bg)}
.footer .brand{left:155px;top:90px;color:var(--teal);font-size:38px}
.footer .brand-dot{width:64px;height:64px;border:3px solid var(--teal)}
.f-col{position:absolute;top:68px}
.f-col h4{font-size:21px;font-weight:400;color:#333;margin-bottom:14px}
.f-col li{list-style:none;font-size:14px;color:#555;margin:0 0 12px 6px}
.social{display:flex;gap:8px}
.social span{width:38px;height:38px;border:2px solid var(--teal);border-radius:50%}
.copy{position:absolute;left:0;top:2978px;width:1200px;height:68px;background:var(--bar-bg);display:flex;align-items:center;justify-content:center;font-size:14px;color:#444}
</style>
</head>
<body>

<header class="hero">
  <div class="brand"><span class="brand-dot"></span>Brelkit</div>
  <nav class="nav">
    <span class="active">Home</span><span>About Us</span><span>Services</span><span>Technology</span><span>Projects</span><span>Support</span><span>Contact</span>
  </nav>
  <div class="abs hero-visual" role="img" aria-label="Photo of a laptop showing code over a teal workspace scene"></div>
  <h1 class="abs hero-title"><span class="big">Web Technology to</span><span class="mid">Easy Creation of Applications</span></h1>
  <p class="abs hero-text">Aget tempor cursus neque mi consectetuer mi a ultricies massa est sed nisl Class aptent taciti sociosqu</p>
  <span class="btn btn-light" style="left:145px;top:402px;width:138px;height:42px">Read More</span>
  <span class="arrow-circle" style="left:39px"><svg width="14" height="20" viewBox="0 0 14 20"><path d="M11 2 3 10l8 8" fill="none" stroke="#fff" stroke-width="2.5"/></svg></span>
  <span class="arrow-circle" style="left:1103px"><svg width="14" height="20" viewBox="0 0 14 20"><path d="M3 2l8 8-8 8" fill="none" stroke="#fff" stroke-width="2.5"/></svg></span>
</header>

<section class="what-we-do">
  <h2 class="heading" style="top:642px">What We Do</h2>
  <svg class="divider" style="top:686px" viewBox="0 0 300 30"><line x1="0" y1="15" x2="128" y2="15" stroke="#2ea58f"/><line x1="172" y1="15" x2="300" y2="15" stroke="#2ea58f"/><g transform="translate(150 15)" fill="none" stroke="#2ea58f" stroke-width="2"><circle r="8"/><circle r="3.5"/><path d="M0-13v4M0 9v4M-13 0h4M9 0h4M-9-9l3 3M6 6l3 3M9-9l-3 3M-6 6l-3 3"/></g></svg>
  <p class="abs wwd-text">Fusce ultricies orci ac feugiat suscipit leo massa sodales velit et scelerisque mi tortor at ipsum cligula augue bibendum accumsan vestibulum ut commodo a mi Morbi ornare gravida elit Integer congue augue et malesuada iaculis ipsum dui aliquet felis at cursus magna nisl nec</p>
  <span class="btn btn-teal" style="left:530px;top:834px;width:140px;height:42px">Read More</span>
  <div class="abs wwd-visual" role="img" aria-label="Line illustration of an industrial machine with conveyor belts and pipes"></div>
</section>

<section class="why">
  <h2 class="abs why-title">Why We Are</h2>
  <div class="abs why-text">
    <p>Fusce ultricies orci ac feugiat suscipit leo massa sodales velit et scelerisque mi tortor at ipsum cligula augue bibendum accumsan vestibulum ut commodo a mi</p>
    <p>Morbi ornare gravida elit Integer congue augue et malesuada iaculis ipsum dui aliquet felis at cursus magna nisl nec</p>
  </div>
  <span class="btn btn-light" style="left:122px;top:303px;width:124px;height:40px">Read More</span>
  <div class="abs why-visual" role="img" aria-label="Laptop screen showing the runtime architecture diagram"></div>
</section>

<section class="projects">
  <h2 class="heading" style="top:1654px;color:var(--teal)">Our Projects</h2>
  <svg class="divider" style="top:1700px" viewBox="0 0 300 30"><line x1="0" y1="15" x2="128" y2="15" stroke="#2ea58f"/><line x1="172" y1="15" x2="300" y2="15" stroke="#2ea58f"/><g transform="translate(150 15)" fill="none" stroke="#2ea58f" stroke-width="2"><circle r="8"/><circle r="3.5"/><path d="M0-13v4M0 9v4M-13 0h4M9 0h4M-9-9l3 3M6 6l3 3M9-9l-3 3M-6 6l-3 3"/></g></svg>
  <article class="card" style="left:130px">
    <div class="card-img" role="img" aria-label="Photo of hands using a glowing tablet"></div>
    <h3 class="card-title">Project Title here</h3>
    <p class="card-text">Class aptent taciti sociosqu ad litora torquent per conubia nostra per inceptos</p>
    <span class="arrow-circle"><svg width="12" height="16" viewBox="0 0 12 16"><path d="M3 2l6 6-6 6" fill="none" stroke="#fff" stroke-width="2.5"/></svg></span>
  </article>
  <article class="card" style="left:452px">
    <div class="card-img" style="background:linear-gradient(135deg,#101a2a,#24405e)" role="img" aria-label="Photo of source code on a dark screen"></div>
    <h3 class="card-title">Project Title here</h3>
    <p class="card-text">Class aptent taciti sociosqu ad litora torquent per conubia nostra per inceptos</p>
    <span class="arrow-circle"><svg width="12" height="16" viewBox="0 0 12 16"><path d="M3 2l6 6-6 6" fill="none" stroke="#fff" stroke-width="2.5"/></svg></span>
  </article>
  <article class="card" style="left:773px">
    <div class="card-img" style="background:linear-gradient(135deg,#2b2d33,#8a7a6a)" role="img" aria-label="Photo of a person typing code on a laptop"></div>
    <h3 class="card-title">Project Title here</h3>
    <p class="card-text">Class aptent taciti sociosqu ad litora torquent per conubia nostra per inceptos</p>
    <span class="arrow-circle"><svg width="12" height="16" viewBox="0 0 12 16"><path d="M3 2l6 6-6 6" fill="none" stroke="#fff" stroke-width="2.5"/></svg></span>
  </article>
</section>

<section class="testi">
  <h2 class="heading" style="top:20px;color:var(--white)">Testimonials</h2>
  <svg class="divider" style="top:63px" viewBox="0 0 300 30"><line x1="0" y1="15" x2="128" y2="15" stroke="#fff"/><line x1="172" y1="15" x2="300" y2="15" stroke="#fff"/><g transform="translate(150 15)" fill="none" stroke="#fff" stroke-width="2"><circle r="8"/><circle r="3.5"/><path d="M0-13v4M0 9v4M-13 0h4M9 0h4M-9-9l3 3M6 6l3 3M9-9l-3 3M-6 6l-3 3"/></g></svg>
  <span class="arrow-circle" style="left:50px"><svg width="12" height="16" viewBox="0 0 12 16"><path d="M9 2 3 8l6 6" fill="none" stroke="#fff" stroke-width="2.5"/></svg></span>
  <span class="arrow-circle" style="left:1112px"><svg width="12" height="16" viewBox="0 0 12 16"><path d="M3 2l6 6-6 6" fill="none" stroke="#fff" stroke-width="2.5"/></svg></span>
  <blockquote class="quote" style="left:117px">
    <span class="avatar" role="img" aria-label="Portrait of Wenna Ostrick"></span>
    <p>Nam libero tempore, cum soluta nobis est eligendi optio cumque nihil impedit quo minus id quod maxime placeat facere possi mus, omnis voluptas assumend</p>
    <div class="name">Wenna Ostrick</div>
  </blockquote>
  <blockquote class="quote" style="left:451px">
    <span class="avatar" role="img" aria-label="Portrait of Dalia Fenwright"></span>
    <p>Nam libero tempore, cum soluta nobis est eligendi optio cumque nihil impedit quo minus id quod maxime placeat facere possi mus, omnis voluptas assumend</p>
    <div class="name">Dalia Fenwright</div>
  </blockquote>
  <blockquote class="quote" style="left:787px">
    <span class="avatar" role="img" aria-label="Portrait of Corin Ashvale"></span>
    <p>Nam libero tempore, cum soluta nobis est eligendi optio cumque nihil impedit quo minus id quod maxime placeat facere possi mus, omnis voluptas assumend</p>
    <div class="name">Corin Ashvale</div>
  </blockquote>
</section>

<section class="partners">
  <span>VANTRO</span><span>Mellory</span><span>QUILLON</span><span>Oskava</span><span>tallow</span><span>BRISKEN</span>
</section>

<footer class="footer">
  <div class="brand"><span class="brand-dot"></span>Brelkit</div>
  <div class="f-col" style="left:435px">
    <h4>Quick Links</h4>
    <ul><li>Home</li><li>Our Services</li><li>About Us</li><li>Projects</li></ul>
  </div>
  <div class="f-col" style="left:640px">
    <h4>Resources</h4>
    <ul><li>Technology</li><li>Support</li><li>Testimonials</li><li>Contact Us</li></ul>
  </div>
  <div class="f-col" style="left:853px">
    <h4>Follow Us</h4>
    <div class="social" aria-label="Social links"><span></span><span></span><span></span><span></span></div>
  </div>
</footer>
<div class="copy">© 2018 Company Name &nbsp;All right reserved</div>

</body>
</html>
```